Health Clinic treating people with mental illness needs a website

We need a website for a new mental health clinic based in Florida called Tidewell Balance USA. We treat people with mental health issues such as depression, PTSD, Bipolar, chronic pain, etc. I want the website to be easy to follow and inviting to the visitors. It should be easy to locate the different treatment options and how to go about contacting and making appointments. The images on the website should be something that the patients can relate to, whether a close up of a woman's face, something that conveys emotion. The patients visiting this website are often sad and miserable, they need to be able to feel comfortable when they look at this website. I want them to feel that we understand where they are coming from. I like colors such as purple, turquoise, lavender.

Target Market(s)

College students, veterans, anyone with mental illness

Industry/Entity Type

Health And Wellness

Font styles to use
Serif
Sans Serif

Colors

Designer to choose colors to be used in the design.

Requirements
Must have
• There should be a home/landing page, about us page, treatment page, contact page, and a FAQ page. I've included my logo below.
Nice to have
• The flow of the web pages should be calming and welcoming. I want people to feel warm and understood when they enter our page.
Should not have
• The images and writing should not be overly stimulating or aggressive.

```html
<!DOCTYPE html>
<html lang="en">
<head>
<meta charset="utf-8">
<title>Tidewell Balance USA</title>
<link href="https://fonts.googleapis.com/css2?family=Libre+Baskerville:ital,wght@0,400;0,700;1,400&family=Poppins:wght@300;400;500;600&display=swap" rel="stylesheet">
<style>
:root{
  --teal:#34b5a0;
  --teal-dark:#2a9e8b;
  --purple:#6a3f98;
  --purple-dark:#4d2a73;
  --lavender:#e4daef;
  --lavender-soft:#f6f3fa;
  --ink:#333;
  --muted:#888;
  --white:#fff;
  --serif:'Libre Baskerville', Georgia, serif;
  --sans:'Poppins', Arial, sans-serif;
}
*{box-sizing:border-box;margin:0;padding:0}
html,body{width:1200px;height:3527px;overflow:hidden}
body{position:relative;font-family:var(--sans);color:var(--ink);background:var(--white)}
.abs{position:absolute}
a{color:inherit;text-decoration:none}

/* top bar */
.topbar{left:0;top:0;width:1200px;height:33px;background:var(--teal);color:var(--white);font-size:11px}
.topbar .info{left:160px;top:9px;display:flex;gap:24px;align-items:center}
.topbar .info span{display:flex;align-items:center;gap:6px}
.topbar .cta{left:868px;top:0;width:181px;height:33px;background:var(--purple);text-align:center;line-height:33px;text-transform:uppercase;font-size:11px;letter-spacing:.5px}

/* nav */
.nav{left:0;top:33px;width:1200px;height:85px;background:var(--white)}
.brand{left:160px;top:22px;display:flex;align-items:center;gap:8px}
.brand .dot{width:14px;height:14px;border-radius:50%;background:var(--teal)}
.brand .name{font-family:var(--serif);font-weight:700;font-size:18px;color:var(--purple)}
.menu{left:0;top:0;width:1200px;height:85px}
.menu a{position:absolute;top:42px;font-size:13px;color:#444}
.menu a.active{color:var(--teal)}
.menu a.active::after{content:"";position:absolute;left:0;right:0;bottom:-8px;height:2px;background:var(--teal)}

/* hero */
.hero{left:0;top:118px;width:1200px;height:620px;background:linear-gradient(100deg,#8c6a55 0%,#b48f78 28%,#7a7050 48%,#4f6b34 66%,#3d5a26 100%)}
.hero-shade{left:0;top:118px;width:1200px;height:620px;background:rgba(20,20,20,.28)}
.hero-title{left:0;top:425px;width:1200px;text-align:center;color:var(--white);font-size:30px;font-weight:300;line-height:38px;text-transform:uppercase;letter-spacing:1px}
.btn{height:40px;line-height:40px;text-align:center;color:var(--white);font-size:12px;text-transform:uppercase;letter-spacing:.5px}
.btn.teal{background:var(--teal)}
.btn.purple{background:var(--purple)}
.hero-ring{left:580px;top:278px;width:40px;height:40px;border:1px solid rgba(255,255,255,.6);border-radius:50%}

/* welcome */
.eyebrow{font-size:14px;color:var(--purple);text-align:center}
.section-title{font-family:var(--serif);color:var(--purple);text-align:center}
.feature{top:887px;width:271px;height:203px;background:var(--lavender-soft);border:1px solid #e2dce8;box-shadow:0 2px 6px rgba(0,0,0,.06);padding:24px 20px}
.feature svg{display:block;margin-bottom:22px}
.feature h3{font-family:var(--serif);font-weight:400;font-size:14px;margin-bottom:18px;color:#333}
.feature p{font-size:10.5px;line-height:16px;color:#555}

/* visit / appointment */
.visit{left:179px;top:1196px;width:380px;color:var(--white)}
.visit .small{font-family:var(--serif);font-size:17px}
.visit .big{font-family:var(--serif);font-size:22px;text-transform:uppercase;margin-top:2px}
.visit p{font-size:10.5px;line-height:17px;margin-top:24px}
.hours{margin-top:26px;font-size:10.5px;font-weight:500}
.hours div{display:flex;height:21px}
.hours span:first-child{width:155px}
.appt{left:630px;top:1196px;color:var(--white)}
.field{position:absolute;height:27px;background:var(--white);border:1px solid #d7e9e5;font-size:9px;color:#aaa;padding:8px 6px}
.send{position:absolute;left:630px;top:1431px;width:70px;height:26px;background:var(--white);color:var(--teal);font-size:10px;text-align:center;line-height:26px;text-transform:uppercase}

/* services */
.svc-head{left:176px;top:1584px}
.svc-head .small{font-family:var(--serif);font-size:20px;color:var(--purple)}
.svc-head .big{font-family:var(--serif);font-size:22px;color:var(--purple);text-transform:uppercase;margin-top:4px}
.svc-intro{left:176px;top:1644px;width:460px;font-size:10.5px;line-height:16px;color:var(--muted)}
.svc-item{width:195px}
.svc-item .num{font-size:10px;color:#ccc}
.svc-item h4{font-family:var(--serif);font-weight:400;font-size:14px;color:var(--purple);margin:6px 0 8px}
.svc-item p{font-size:10.5px;line-height:16px;color:#555}
.svc-back{left:711px;top:1711px;width:310px;height:353px;background:var(--lavender)}
.svc-media{left:624px;top:1664px;width:367px;height:364px;background:linear-gradient(180deg,#8c7aa6 0%,#9c86b4 50%,#6b5682 80%,#2b2233 100%)}
.play{left:782px;top:1830px;width:50px;height:34px;background:var(--white);border-radius:6px}

/* stories */
.sub{font-size:10.5px;line-height:16px;color:var(--muted);text-align:center}
.story{left:235px;top:2254px;width:730px;height:252px;background:#f7f6f8}
.story-photo{left:235px;top:2254px;width:306px;height:252px;background:linear-gradient(135deg,#e9e6e1 0%,#d9d2c9 55%,#c4bcb3 100%)}
.story-name{left:579px;top:2322px;font-size:12px;font-weight:600;color:var(--purple)}
.story-text{left:579px;top:2350px;width:360px;font-family:var(--serif);font-style:italic;font-size:11px;line-height:19px;color:#555}
.dots{left:579px;top:2464px;display:flex;gap:6px}
.dots i{display:block;width:10px;height:3px;background:#ccc}
.dots i.on{width:22px;background:#555}

/* posts */
.post{top:2711px;width:233px;height:247px;background:var(--white);box-shadow:0 2px 8px rgba(0,0,0,.08)}
.post-img{height:125px}
.post-body{padding:12px 14px}
.post h5{font-family:var(--serif);font-size:12px;line-height:18px;color:#222}
.post .cat{font-size:10px;color:var(--muted);margin-top:6px;padding-bottom:10px;border-bottom:1px solid #ddd}
.post .meta{font-size:9px;color:var(--muted);margin-top:8px;display:flex;gap:14px}

/* footer */
.footer{left:0;top:3082px;width:1200px;height:412px;background:var(--purple);color:var(--white)}
.sub-title{left:0;top:3122px;width:1200px;text-align:center;font-family:var(--serif);font-size:18px}
.sub-note{left:0;top:3156px;width:1200px;text-align:center;font-size:10px;color:#a88fc6}
.sub-input{left:428px;top:3184px;width:341px;height:24px;background:var(--white);font-size:10px;color:#777;padding:5px 10px}
.foot-h{font-size:11px;text-transform:uppercase;letter-spacing:.5px}
.links{font-size:10px;line-height:30px}
.links li{list-style:none;display:flex;align-items:center;gap:8px}
.links li::before{content:"";width:4px;height:4px;border-radius:50%;background:var(--white)}
.tweet{width:280px;font-size:10px;line-height:15px;display:flex;gap:12px}
.tweet i{flex:0 0 12px;height:12px;border-radius:50%;background:var(--white);margin-top:2px}
.contact{font-size:10px;line-height:15px}
.bottom{left:0;top:3494px;width:1200px;height:33px;background:var(--purple-dark);color:var(--white);font-size:10px}
.social{left:898px;top:11px;display:flex;gap:14px}
.social i{display:block;width:11px;height:11px;background:var(--white)}
</style>
</head>
<body>

<!-- top bar -->
<div class="abs topbar">
  <div class="abs info">
    <span><svg width="12" height="9" viewBox="0 0 12 9"><rect x=".5" y=".5" width="11" height="8" fill="none" stroke="#fff"/><path d="M.5 .5 6 5l5.5-4.5" fill="none" stroke="#fff"/></svg>info@tidewellbalance.com</span>
    <span><svg width="11" height="11" viewBox="0 0 11 11"><circle cx="5.5" cy="5.5" r="5" fill="none" stroke="#fff"/><path d="M5.5 2.5v3h2" fill="none" stroke="#fff"/></svg>Mon - Sat : 10:00am - 7:00 PM</span>
  </div>
  <a class="abs cta" href="#appointment">Get an appointment</a>
</div>

<!-- navigation -->
<header class="abs nav">
  <div class="abs brand"><span class="dot"></span><span class="name">Tidewell Balance USA</span></div>
  <nav class="abs menu">
    <a class="active" style="left:575px" href="#">Home</a>
    <a style="left:652px" href="#">About Us</a>
    <a style="left:748px" href="#">Service</a>
    <a style="left:834px" href="#">History</a>
    <a style="left:919px" href="#">FAQs</a>
    <a style="left:988px" href="#">Contact</a>
  </nav>
</header>

<!-- hero -->
<div class="abs hero" role="img" aria-label="Close-up photo of a thoughtful young woman with her hand near her face, green foliage behind"></div>
<div class="abs hero-shade"></div>
<div class="abs hero-ring"></div>
<h1 class="abs hero-title">Life is not for a moment<br>but its a combination of moments</h1>
<a class="abs btn teal" style="left:414px;top:536px;width:172px" href="#">Know more</a>
<a class="abs btn purple" style="left:607px;top:536px;width:172px" href="#">Book a session</a>
<svg class="abs" style="left:0;top:640px" width="1200" height="110" viewBox="0 0 1200 110">
  <polygon points="0,40 600,96 1200,40 1200,110 0,110" fill="#fff"/>
  <polyline points="0,46 600,100 1200,46" fill="none" stroke="#d7f0ec" stroke-width="6"/>
  <polyline points="80,58 600,106 1120,58" fill="none" stroke="#e4daef" stroke-width="2"/>
  <circle cx="600" cy="38" r="26" fill="#6a3f98"/>
  <polyline points="590,33 600,43 610,33" fill="none" stroke="#fff" stroke-width="3"/>
</svg>

<!-- welcome -->
<div class="abs eyebrow" style="left:0;top:790px;width:1200px">welcome to</div>
<h2 class="abs section-title" style="left:0;top:812px;width:1200px;font-size:30px;font-weight:400;letter-spacing:1px">TIDEWELL</h2>

<div class="abs feature" style="left:169px">
  <svg width="40" height="36" viewBox="0 0 40 36"><path d="M6 12h22v10a9 9 0 0 1-9 9h-4a9 9 0 0 1-9-9z M28 15h4a4 4 0 0 1 0 8h-4 M4 34h28 M12 3v5 M17 2v6 M22 3v5" fill="none" stroke="#ccc" stroke-width="1.5"/></svg>
  <h3>Talking about Problems</h3>
  <p>We listen first, without hurry or judgement, so you can share what weighs on you at your own pace.</p>
</div>
<div class="abs feature" style="left:463px">
  <svg width="40" height="36" viewBox="0 0 40 36"><rect x="2" y="10" width="20" height="14" fill="none" stroke="#ccc" stroke-width="1.5"/><rect x="14" y="2" width="22" height="14" fill="none" stroke="#ccc" stroke-width="1.5"/><path d="M6 24v6l6-6" fill="none" stroke="#ccc" stroke-width="1.5"/></svg>
  <h3>Ongoing Discussion</h3>
  <p>Regular sessions keep the conversation open, with care that adapts as your needs change over time.</p>
</div>
<div class="abs feature" style="left:758px">
  <svg width="40" height="36" viewBox="0 0 40 36"><circle cx="18" cy="19" r="15" fill="none" stroke="#ccc" stroke-width="1.5"/><circle cx="18" cy="19" r="9" fill="none" stroke="#ccc" stroke-width="1.5"/><circle cx="18" cy="19" r="3" fill="none" stroke="#ccc" stroke-width="1.5"/><path d="M18 19 36 3 M31 3h5v5" fill="none" stroke="#ccc" stroke-width="1.5"/></svg>
  <h3>Solving the Problem.</h3>
  <p>Together we build a clear plan of treatment and steady steps toward lasting relief and balance.</p>
</div>

<!-- visit / appointment -->
<svg class="abs" style="left:0;top:1165px" width="1200" height="355" viewBox="0 0 1200 355">
  <polygon points="0,5 600,38 600,348 0,325" fill="#6a3f98"/>
  <polygon points="600,38 1200,5 1200,325 600,348" fill="#34b5a0"/>
</svg>
<section class="abs visit">
  <div class="small">When you</div>
  <div class="big">Can visit us</div>
  <p>Our doors are open to students, veterans and anyone who needs support. Drop by our calm Florida clinic or call ahead so a caring member of our team can welcome you in person.</p>
  <div class="hours">
    <div><span>Monday - Friday</span><span>9.15 am - 5.30 pm</span></div>
    <div><span>Saturday</span><span>Closed</span></div>
    <div><span>Sunday</span><span>Closed</span></div>
  </div>
</section>
<section class="abs appt" id="appointment">
  <div style="font-family:var(--serif);font-size:17px">Make</div>
  <div style="font-family:var(--serif);font-size:22px;text-transform:uppercase;margin-top:2px">An appointment</div>
</section>
<div class="field" style="left:630px;top:1252px;width:273px">Name</div>
<div class="field" style="left:630px;top:1286px;width:133px">Email</div>
<div class="field" style="left:770px;top:1286px;width:133px">Phone</div>
<div class="field" style="left:630px;top:1320px;width:133px">Subject</div>
<div class="field" style="left:770px;top:1320px;width:133px">Available Date</div>
<div class="field" style="left:630px;top:1356px;width:273px;height:62px">Tell us a little more</div>
<div class="send">Send</div>

<!-- services -->
<div class="abs svc-head"><div class="small">Our</div><div class="big">Services</div></div>
<p class="abs svc-intro">Gentle, evidence-based care for the conditions our patients face, offered by a team that understands where you are coming from.</p>

<div class="abs svc-item" style="left:176px;top:1718px"><div class="num">01</div><h4>Chronic Pain</h4><p>Relief plans that ease lasting pain and help you return to the days you enjoy.</p></div>
<div class="abs svc-item" style="left:402px;top:1718px"><div class="num">02</div><h4>PTSD</h4><p>Trauma-aware sessions for veterans and others carrying hard memories each day.</p></div>
<div class="abs svc-item" style="left:176px;top:1829px"><div class="num">03</div><h4>Major Depression</h4><p>Steady support and treatment that lift heavy moods, one careful step at a time.</p></div>
<div class="abs svc-item" style="left:402px;top:1829px"><div class="num">04</div><h4>Anxiety Therapy</h4><p>Calm, practical tools to quiet worry and restore a sense of safety and rest.</p></div>
<div class="abs svc-item" style="left:176px;top:1940px"><div class="num">05</div><h4>Hypnotherapy</h4><p>Guided relaxation that helps the mind settle and open up to healthy change.</p></div>
<div class="abs svc-item" style="left:402px;top:1940px"><div class="num">06</div><h4>IV nutrition therapy</h4><p>Gentle infusions that restore key nutrients to support body and mind alike.</p></div>

<div class="abs svc-back"></div>
<div class="abs svc-media" role="img" aria-label="Video still of a person in a yoga pose silhouetted against a violet dusk sky"></div>
<div class="abs play"></div>
<svg class="abs" style="left:800px;top:1838px" width="14" height="18" viewBox="0 0 14 18"><polygon points="0,0 14,9 0,18" fill="#222"/></svg>

<!-- success stories -->
<h2 class="abs section-title" style="left:0;top:2134px;width:1200px;font-size:22px;font-weight:400">Success Stories</h2>
<p class="abs sub" style="left:400px;top:2176px;width:400px">Real words from people who found their footing again with the gentle help of our caring team.</p>
<div class="abs story"></div>
<div class="abs story-photo" role="img" aria-label="Photo of a smiling woman seated at a desk with a laptop"></div>
<div class="abs story-name">Mara Ellison</div>
<p class="abs story-text">I came in feeling lost and tired of everything. The team listened, never rushed me, and built a plan that fit my life. Today I sleep better, laugh more and finally feel like myself again. I am so thankful.</p>
<div class="abs dots"><i></i><i class="on"></i><i></i></div>

<!-- latest posts -->
<h2 class="abs section-title" style="left:0;top:2595px;width:1200px;font-size:22px;font-weight:400">Latest Post</h2>
<p class="abs sub" style="left:400px;top:2637px;width:400px">Notes, guides and stories from our clinicians to help you understand and care for your mind.</p>

<article class="abs post" style="left:235px">
  <div class="post-img" role="img" aria-label="Photo of a small group therapy session in a bright room" style="background:linear-gradient(135deg,#e6e1da,#cfc4b6)"></div>
  <div class="post-body"><h5>Depression affects children's mental development</h5><div class="cat">Stress Management</div><div class="meta"><span>December 26, 2017</span><span>No Comments</span></div></div>
</article>
<article class="abs post" style="left:485px">
  <div class="post-img" role="img" aria-label="Photo of a patient resting on a couch while a therapist takes notes" style="background:linear-gradient(135deg,#e2e4e6,#bfc3c6)"></div>
  <div class="post-body"><h5>Anxiety disorder affects human life very badly</h5><div class="cat">Drug Abuse</div><div class="meta"><span>December 26, 2017</span><span>No Comments</span></div></div>
</article>
<article class="abs post" style="left:736px">
  <div class="post-img" role="img" aria-label="Photo of a psychologist talking with a circle of people" style="background:linear-gradient(135deg,#ebe6e1,#c9bfb8)"></div>
  <div class="post-body"><h5>Session with psychologist can change the relationship</h5><div class="cat">Depression</div><div class="meta"><span>December 26, 2017</span><span>No Comments</span></div></div>
</article>

<!-- footer -->
<footer class="abs footer"></footer>
<div class="abs sub-title">Subscribe Newsletter</div>
<div class="abs sub-note">Get our latest updates in your inbox</div>
<div class="abs sub-input">Type your email id</div>
<svg class="abs" style="left:740px;top:3191px" width="13" height="10" viewBox="0 0 13 10"><rect x=".5" y=".5" width="12" height="9" fill="none" stroke="#6a3f98"/><path d="M.5 .5 6.5 5.5 12.5 .5" fill="none" stroke="#6a3f98"/></svg>

<div class="abs foot-h" style="left:176px;top:3248px">Useful Links</div>
<ul class="abs links" style="left:176px;top:3278px"><li>Home</li><li>About Us</li><li>History</li><li>Contact</li><li>Blog</li></ul>
<ul class="abs links" style="left:299px;top:3278px"><li>Book Session</li><li>Services</li><li>FAQs</li><li>Success Stories</li></ul>

<div class="abs foot-h" style="left:487px;top:3248px">Twitter Feed</div>
<div class="abs tweet" style="left:487px;top:3286px"><i></i><span>Harbor Lane Studio Notes - small steps count. A calm morning routine can ease anxious thoughts and set a kinder tone for the day. Read more on our blog yesterday</span></div>
<div class="abs tweet" style="left:487px;top:3356px"><i></i><span>Harbor Lane Studio Notes - reaching out is brave. Our team is here to listen whenever you feel ready to talk and plan your care. Learn more yesterday</span></div>

<div class="abs foot-h" style="left:831px;top:3248px">Contact Info</div>
<div class="abs contact" style="left:831px;top:3284px">48 Bayview Road, Harbor City,<br>FL, USA<br><br>+1(555) 014 786<br>+1(555) 014 654<br><br>info@tidewellbalance.com<br>www.tidewellbalance.com</div>

<div class="abs bottom">
  <div class="abs" style="left:170px;top:10px">@2018, All Right Reserved Tidewell Balance USA</div>
  <div class="abs social"><i></i><i></i><i></i><i></i><i></i></div>
</div>

</body>
</html>
```